Lumora business card for a plastic surgeon

we need a business card for plastic surgeons that work on a clinic called LUMORA.
we want a clean design and the following informations: name of the doctor, doctor's registration number (called CRM), telephone, address, facebook, instagram.
Colors: white, blue tones, light brown/ coffee

facebook and instagram: lumoracirurgiaestetica

Industry/Entity Type

Business

Contact Information for Business Card

clean design

Font styles to use
Serif
Sans Serif
Other font styles liked:
• helvetica light

Colors
cee9f5
85cae6
85abd2
3276b5
cfeae6
cedeed
eaf1f7

Requirements
Must have
• doctor's name
• identification number (called CRM)
• contact (phone, facebook, instagram, address)

```html
<!DOCTYPE html>
<html lang="pt">
<head>
<meta charset="utf-8">
<title>Lumora – Business Card</title>
<link rel="stylesheet" href="https://fonts.googleapis.com/css2?family=Cinzel:wght@400&family=Tinos&family=Roboto:wght@300&display=swap">
<style>
  :root {
    --page-bg: #eeefee;
    --card-white: #ffffff;
    --card-navy: #103a63;
    --brand-cyan: #35b6dc;
    --text-navy: #1f3c66;
    --text-white: #ffffff;
  }
  html, body {
    margin: 0;
    padding: 0;
    width: 1200px;
    height: 1023px;
    overflow: hidden;
    background: var(--page-bg);
  }
  .canvas {
    position: relative;
    width: 1200px;
    height: 1023px;
  }
  .card {
    position: absolute;
    width: 546px;
    height: 312px;
  }
  .card--front {
    left: 116px;
    top: 141px;
    background: var(--card-white);
  }
  .card--back {
    left: 510px;
    top: 536px;
    background: var(--card-navy);
  }
  .front-content {
    position: absolute;
    left: 0;
    right: 0;
    top: 56px;
    text-align: center;
  }
  .brand-name {
    margin: 0;
    font-family: "Cinzel", serif;
    font-weight: 400;
    font-size: 42px;
    line-height: 48px;
    letter-spacing: 1px;
    color: var(--brand-cyan);
  }
  .brand-tagline {
    margin: 2px 0 0;
    font-family: "Tinos", serif;
    font-size: 15px;
    line-height: 18px;
    letter-spacing: 1px;
    color: var(--text-navy);
  }
  .doctor-name {
    margin: 14px 0 0;
    font-family: "Tinos", serif;
    font-size: 29px;
    line-height: 32px;
    color: var(--brand-cyan);
  }
  .contact {
    margin: 0;
    font-family: "Roboto", sans-serif;
    font-weight: 300;
    font-size: 14.5px;
    line-height: 18px;
    color: var(--text-navy);
  }
  .contact--address {
    margin-top: 8px;
  }
  .social-list {
    position: absolute;
    left: 187px;
    top: 128px;
    margin: 0;
    padding: 0;
    list-style: none;
  }
  .social-item {
    display: flex;
    align-items: center;
    height: 20px;
    margin-bottom: 16px;
    font-family: "Roboto", sans-serif;
    font-weight: 300;
    font-size: 15px;
    color: var(--text-white);
  }
  .social-mark {
    width: 18px;
    height: 18px;
    margin-right: 5px;
    background: var(--text-white);
    border-radius: 2px;
  }
</style>
</head>
<body>
  <main class="canvas">
    <section class="card card--front" aria-label="Card front">
      <div class="front-content">
        <h1 class="brand-name">LUMORA</h1>
        <p class="brand-tagline">CIRURGIA PLÁSTICA</p>
        <h2 class="doctor-name">John Doe</h2>
        <p class="contact">45678</p>
        <p class="contact">555 555 555</p>
        <p class="contact contact--address">48 North Harbor Lane<br>Fort Lauderdale, FL 33304</p>
      </div>
    </section>

    <section class="card card--back" aria-label="Card back">
      <ul class="social-list">
        <li class="social-item"><span class="social-mark" aria-hidden="true"></span>lumoracirurgiaestetica</li>
        <li class="social-item"><span class="social-mark" aria-hidden="true"></span>lumoracirurgiaestetica</li>
      </ul>
    </section>
  </main>
</body>
</html>
```